Skorlev, Denmark - book cover design

Front cover design for Danish novel being translated into English

Author: Søren Kjeld Hvidtoft
Title in English: Skorlev, Denmark

Blurb (please forgive the Google translate):
In Skorlev, Denmark, where you really follow people's comings and goings, Tove Salk has settled down with her daughter Signe and her husband Torben. The family comes from the capital Copenhagen and is definitely outcasts in the small town community. Tove feels undersimulated both intellectually and sexually. Therefore, she seeks distraction by stealing in the local co-op. However, she doesn’t know that the shopkeeper Henning is keeping an eye on her - and has big plans.
As a reader, you are sucked into the backwaters of Jutland so much so that it almost hurts. Vandel is captivating entertainment that takes place on an authentic background, and one can’t help but feel a certain sympathy towards the victims that are drawn into the story’s dramatic spiral.

Attached is the original Danish book cover as well as a map of Denmark showing the location of the small town of Vandel. Please use the map as a guideline for cover design since Vandel is a Black spot on most English speakers' world map. Vandel and Copenhagen are marked on the map.

Target Market(s)

English speaking markets

Colors

Designer to choose colors to be used in the design.

Requirements
Nice to have
• A map of Denmark marking/naming Copenhagen and Vandel

```html
<!DOCTYPE html>
<html lang="en">
<head>
<meta charset="utf-8">
<title>Skorlev, Denmark – Søren Kjeld Hvidtoft</title>
<link rel="stylesheet" href="https://fonts.googleapis.com/css2?family=Josefin+Sans:wght@300;600&display=swap">
<style>
  :root {
    --sky-cream: #f2dcc8;
    --surf-pink: #e6bfae;
    --sand-plum: #8a5873;
    --dune-green: #6f6a45;
    --grass-olive: #857a4e;
    --board-rose: #d9a393;
    --board-shadow: #9a6479;
    --ink-plum: #3a2438;
    --chalk: rgba(236, 228, 238, 0.82);
  }
  html, body {
    margin: 0;
    padding: 0;
    width: 1162px;
    height: 1200px;
    overflow: hidden;
    background: var(--sky-cream);
  }
  .cover {
    position: relative;
    width: 1162px;
    height: 1200px;
    overflow: hidden;
  }
  .cover-photo {
    position: absolute;
    inset: 0;
    background:
      radial-gradient(ellipse 70% 45% at 78% 82%, rgba(232, 176, 160, 0.9), rgba(232, 176, 160, 0) 70%),
      linear-gradient(180deg,
        var(--sky-cream) 0%,
        var(--surf-pink) 7%,
        var(--sand-plum) 12%,
        var(--sand-plum) 15%,
        var(--dune-green) 19%,
        var(--grass-olive) 38%,
        #9b7a5e 55%,
        var(--board-shadow) 68%,
        var(--board-rose) 80%,
        #c98e88 100%);
  }
  .author {
    position: absolute;
    top: 8px;
    left: 0;
    right: 0;
    margin: 0;
    text-align: center;
    font-family: "Josefin Sans", sans-serif;
    font-weight: 600;
    font-variant: small-caps;
    font-size: 30px;
    letter-spacing: 1px;
    color: var(--ink-plum);
  }
  .title {
    margin: 0;
    font-family: "Josefin Sans", sans-serif;
    font-weight: 300;
    color: var(--chalk);
  }
  .title-town {
    position: absolute;
    left: 205px;
    top: 395px;
    width: 60px;
    font-size: 58px;
    line-height: 70px;
    text-align: center;
    writing-mode: vertical-rl;
    text-orientation: upright;
    letter-spacing: 6px;
  }
  .title-country {
    position: absolute;
    left: 440px;
    top: 230px;
    font-size: 44px;
    letter-spacing: 6px;
    transform-origin: 0 50%;
    transform: rotate(32deg);
    white-space: nowrap;
  }
</style>
</head>
<body>
  <main class="cover">
    <div class="cover-photo" role="img" aria-label="Faded photograph of a weathered wooden boardwalk and stairs winding through grassy dunes down to a sandy beach and surf"></div>
    <p class="author">Søren Kjeld Hvidtoft</p>
    <h1 class="title" aria-label="Skorlev, Denmark">
      <span class="title-town">SKORLEV</span>
      <span class="title-country">DENMARK</span>
    </h1>
  </main>
</body>
</html>
```